UI/UX Design for AI Photo-to-Video Web Platform (Figma)

I am looking for a modern, high-converting redesign for my Next.js-based web platform. The service allows users to transform old photos into vibrant memories using AI. The design needs to be clean, intuitive, and "mobile-ready" (responsive).
Key Features to Visualize on the Homepage:
Photo Restoration & Colorization: A clear "before/after" visual showing a black-and-white photo turning into a high-quality color photo.
Photo-to-Video Animation: A visual representation of how both B&W and color photos are transformed into dynamic video clips.
Story Creation: A section showing how these photos and videos are combined into a single "Story Video" with background music.
Scope of Work:
Homepage Redesign: A hero section with the core value proposition and a visual walkthrough of the process.
Service/Internal Pages: Redesigning the functional pages where users upload files and manage their projects.
Responsive Design: While the focus is desktop, the layout must be designed with a "Mobile-First" mindset for easy porting to a mobile app later.
Technical Requirements for the Designer:
Tool: Must be designed in Figma.
Structure: Use Figma Auto Layout and Components for all elements (buttons, inputs, cards).
Design System: Provide a clear style guide (Typography, Color Palette, Spacing).
Assets: All icons should be in SVG format.
Style Preference:
Modern, sleek, and trustworthy.
Since the product is about "memories," the vibe should be emotional yet technologically advanced (AI-driven).

```html
<!DOCTYPE html>
<html lang="en">
<head>
<meta charset="utf-8">
<title>memora.ai — page designs</title>
<link href="https://fonts.googleapis.com/css2?family=Lexend:wght@300;400;500;600;700&display=swap" rel="stylesheet">
<style>
:root{
  --canvas:#1e1e1e;
  --page:#060c20;
  --band:#0a1633;
  --card:#0d1b3f;
  --card-line:#1a2c57;
  --text:#f3f6ff;
  --muted:#8290b3;
  --blue:#3b82f6;
  --teal:#2dd4bf;
  --red:#6b1f2e;
  --photo-a:#9a8468;
  --photo-b:#3b3530;
}
*{box-sizing:border-box;margin:0;padding:0}
html,body{width:1200px;height:1200px;overflow:hidden;background:var(--canvas);font-family:'Lexend',sans-serif;color:var(--text)}
.page{position:absolute;background:var(--page);overflow:hidden}
.page > *{position:absolute}
.nav{left:0;top:0;width:269px;height:14px;border-bottom:1px solid #12305a;display:flex;align-items:center;padding:0 21px;font-size:3px;color:var(--muted)}
.nav .logo{font-size:4.4px;font-weight:600;color:var(--text)}
.nav .links{display:flex;gap:8px;margin-left:50px}
.nav .links .on{color:var(--teal);text-decoration:underline}
.nav .auth{margin-left:auto;display:flex;align-items:center;gap:4px}
.btn{display:inline-flex;align-items:center;justify-content:center;background:var(--blue);color:#fff;border-radius:1.5px;font-size:2.6px;padding:0 4px;height:6px}
.btn.ghost{background:transparent;border:.5px solid #3a4a70}
.btn.light{background:#fff;color:var(--blue)}
.eyebrow{font-size:2.2px;color:var(--blue);letter-spacing:.2px;text-transform:uppercase;text-align:center}
.h2{font-size:7px;font-weight:500;text-align:center;width:100%}
.sub{font-size:3px;color:var(--muted);text-align:center;line-height:1.35}
.center{left:0;width:269px}
.card{background:var(--card);border:.5px solid var(--card-line);border-radius:2px}
.step{padding:6px}
.step .icon{width:6px;height:6px;border-radius:1.2px;background:var(--blue);display:block;margin-bottom:4px}
.step b{display:block;font-size:3.2px;font-weight:500;margin-bottom:2px}
.step p{font-size:2.2px;color:var(--muted);line-height:1.35}
.photo{background:linear-gradient(135deg,var(--photo-a),var(--photo-b));border-radius:2px}
.photo.warm{background:linear-gradient(140deg,#c7a265,#4f4a3d 70%)}
.photo.blue{background:linear-gradient(140deg,#4a5b77,#9a8a70)}
.photo.grey{background:linear-gradient(90deg,#cfcfcf 50%,#dcdcdc 50%)}
.drop{border:.6px dashed #3567c8;border-radius:2px;display:flex;flex-direction:column;align-items:center;justify-content:center;gap:2px}
.drop .icon{width:7px;height:7px;background:var(--blue);border-radius:1.5px;margin-bottom:2px}
.drop b{font-size:3.3px;font-weight:500}
.drop small{font-size:2px;color:var(--muted)}
.tag{font-size:1.8px;color:var(--teal);border:.4px solid var(--teal);border-radius:2px;padding:.6px 2px;display:inline-block}
.feature h3{font-size:5.2px;font-weight:500;margin:3px 0 2px}
.feature p{font-size:2.3px;color:var(--muted);line-height:1.4}
.feature ul{list-style:none;font-size:2.2px;margin-top:3px;line-height:1.9}
.feature li:before{content:"•";color:var(--blue);margin-right:2px}
.footer{left:0;width:269px;background:#0a1633;padding:14px 21px 0}
.footer .logo{font-size:4.8px;font-weight:600}
.footer .about{font-size:2.2px;color:var(--muted);width:52px;line-height:1.4;margin-top:2px}
.footer .socials{display:flex;gap:6px;margin-top:5px}
.footer .socials span{width:5px;height:5px;border-radius:50%;background:#2a3a60}
.footer .col{position:absolute;top:14px;font-size:2.3px;color:var(--muted);line-height:3.3}
.footer .col b{color:var(--text);font-weight:500;font-size:2.5px}
.footer .legal{position:absolute;left:21px;right:21px;bottom:8px;border-top:.5px solid #1c2c52;padding-top:5px;display:flex;justify-content:space-between;font-size:2.2px;color:var(--muted)}
.stat{position:absolute;top:12px;width:50px;text-align:center}
.stat b{font-size:10px;font-weight:600;display:block}
.stat small{font-size:2.2px;color:var(--muted)}
.review{padding:5px}
.review .stars{color:#facc15;font-size:3px;letter-spacing:.6px}
.review p{font-size:1.9px;color:var(--muted);line-height:1.4;margin:2px 0}
.review .who{display:flex;align-items:center;gap:2px;font-size:1.9px}
.review .who i{width:4px;height:4px;border-radius:50%;background:#b79b7d;display:block}
.chip{display:inline-block;font-size:2px;border:.4px solid #2d3f6a;border-radius:1.5px;padding:.8px 3px;color:var(--muted)}
.chip.on{background:var(--blue);color:#fff;border-color:var(--blue)}
.field{background:#12234b;border-radius:2px;font-size:2.2px;color:#5e6f96;padding:3px}
.label{font-size:3px;font-weight:500}
.action{width:75px;height:5px;border-radius:1px;background:#2b3d66;font-size:2px;display:flex;align-items:center;justify-content:center}
.action.danger{background:var(--red);color:#e56}
.grad-btn{background:linear-gradient(90deg,var(--blue),var(--teal));border-radius:1.5px;font-size:2px;display:flex;align-items:center;justify-content:center;color:#fff}
</style>
</head>
<body>

<!-- HOME -->
<section class="page" style="left:23px;top:110px;width:269px;height:979px">
  <nav class="nav"><span class="logo">memora.ai</span><span class="links"><span class="on">Home</span><span>Images</span><span>Video animations</span><span>Studio</span></span><span class="auth">Sign in <span class="btn">Get Started</span></span></nav>

  <span class="tag" style="left:21px;top:31px;color:#cfe;border-color:#2a5a70;background:#0f2a44">New: AI Story Videos with Narration</span>
  <h1 style="left:21px;top:38px;font-size:13px;line-height:14.5px;font-weight:600">Bring Your Old<br>Photos<br><span style="background:linear-gradient(90deg,var(--blue),var(--teal));-webkit-background-clip:text;background-clip:text;color:transparent">Back to Life</span></h1>
  <p style="left:21px;top:86px;width:90px;font-size:2.4px;color:var(--muted);line-height:1.4">Restore, colorize, and animate your family memories using cutting-edge AI. Turn damaged photographs into vivid, living stories.</p>
  <span class="btn" style="left:21px;top:102px">Start Free — No Credit Card</span>
  <span class="btn ghost" style="left:66px;top:102px">See How It Works</span>
  <div style="left:21px;top:113px;display:flex;align-items:center;gap:2px;font-size:2px;color:var(--muted)"><span style="width:7px;height:3.5px;border-radius:2px;background:#b79b7d"></span>Trusted by 10,000+ families worldwide</div>
  <div class="photo" role="img" aria-label="Before and after: black and white portrait of a man with a child, right half colorized" style="left:134px;top:31px;width:112px;height:78px;background:linear-gradient(90deg,#6f6f6f,#444 50%,#9c7a5a 50%,#4a3a30)"></div>
  <div style="left:189px;top:31px;width:.6px;height:78px;background:var(--teal)"></div>

  <p class="eyebrow center" style="top:136px">How it works</p>
  <h2 class="h2 center" style="top:142px">Simple. Fast. Stunning.</h2>
  <p class="sub center" style="top:151px">Restore a photo in under 30 seconds — no design skills needed.</p>
  <div class="card step" style="left:22px;top:168px;width:70px;height:37px"><i class="icon"></i><b>Upload Your Photo</b><p>Drag and drop or browse any old photo from your device.</p></div>
  <div class="card step" style="left:99px;top:168px;width:70px;height:37px"><i class="icon"></i><b>AI Enhances It</b><p>Our models restore damage, add color, sharpen details.</p></div>
  <div class="card step" style="left:177px;top:168px;width:70px;height:37px"><i class="icon"></i><b>Share or Animate</b><p>Download your restored photo or create a story video.</p></div>

  <p class="eyebrow center" style="top:231px">Features</p>
  <h2 class="h2 center" style="top:238px">Everything Your Memories Deserve</h2>
  <p class="sub center" style="top:247px">Professional-grade restoration powered by the latest AI models.</p>

  <div class="feature" style="left:21px;top:276px;width:110px"><span class="tag">COLORIZATION</span><h3>Restore &amp; Colorize</h3><p>Transform black and white photographs into vibrant, lifelike color. Our AI understands historical context to apply natural tones.</p><ul><li>Intelligent color mapping</li><li>Skin tone accuracy</li><li>Period-accurate palettes</li></ul></div>
  <div class="photo warm" role="img" aria-label="Colorized street scene with riders on horseback before old buildings" style="left:140px;top:265px;width:107px;height:71px"></div>

  <div class="photo blue" role="img" aria-label="Colorized family portrait of parents with two children" style="left:22px;top:351px;width:107px;height:70px"></div>
  <div class="feature" style="left:140px;top:362px;width:107px"><span class="tag">ANIMATION</span><h3>Animate Memories</h3><p>Bring still photographs to life with subtle, natural motion. Watch your ancestors smile, blink, and turn their heads.</p><ul><li>Natural facial motion</li><li>Smooth frame interpolation</li><li>Export as MP4 or GIF</li></ul></div>

  <div class="feature" style="left:21px;top:448px;width:110px"><span class="tag">STORY VIDEOS</span><h3>Create Story Videos</h3><p>Combine restored photos, animations, and music into a cinematic memory video to share with your family.</p><ul><li>Timeline editor</li><li>Royalty-free music library</li><li>Auto-generated narration</li></ul></div>
  <div class="photo" role="img" aria-label="Colorized portrait of an older man in a suit and hat beside a vintage car" style="left:140px;top:436px;width:107px;height:71px;background:linear-gradient(140deg,#d8d6d0,#3a4a6e 60%,#222)"></div>

  <div class="card" style="left:22px;top:533px;width:225px;height:118px;background:#0a1838"></div>
  <p class="eyebrow center" style="top:545px">Try it free</p>
  <h2 class="h2 center" style="top:551px">Restore Your Photo Now</h2>
  <p class="sub center" style="top:560px">Upload any old photo and watch AI bring it back to life in seconds.</p>
  <div class="drop" style="left:36px;top:575px;width:196px;height:62px"><i class="icon"></i><b>Drop your photo here</b><small>or click to browse your files</small><span class="btn">Choose Photo</span><small>Supports JPG, PNG, HEIC · up to 20MB</small></div>

  <div style="left:0;top:674px;width:269px;height:52px;background:var(--band)"></div>
  <div class="stat" style="left:25px;top:686px"><b>10M+</b><small>Photos Restored</small></div>
  <div class="stat" style="left:81px;top:686px"><b>500K+</b><small>Videos Created</small></div>
  <div class="stat" style="left:140px;top:686px"><b>99.4%</b><small>Satisfaction Rate</small></div>
  <div class="stat" style="left:194px;top:686px"><b>180+</b><small>Countries</small></div>

  <p class="eyebrow center" style="top:748px">Reviews</p>
  <h2 class="h2 center" style="top:754px">Loved by Families Everywhere</h2>
  <p class="sub center" style="top:763px">Real stories from people who've reconnected with their past.</p>
  <div class="card review" style="left:22px;top:779px;width:70px;height:35px"><div class="stars">★★★★★</div><p>"I restored my grandmother's wedding photo and the whole family cried seeing it in color."</p><div class="who"><i></i>Sarah Holland</div></div>
  <div class="card review" style="left:99px;top:779px;width:70px;height:35px"><div class="stars">★★★★★</div><p>"The animation is so natural. It helped my children finally connect with our history."</p><div class="who"><i></i>Marcus Dean</div></div>
  <div class="card review" style="left:177px;top:779px;width:70px;height:35px"><div class="stars">★★★★★</div><p>"We made a story video for my parents' anniversary. Everybody was moved."</p><div class="who"><i></i>Elena Vasquez</div></div>

  <div style="left:22px;top:837px;width:225px;height:47px;border-radius:2px;background:linear-gradient(90deg,var(--blue),var(--teal));text-align:center;padding-top:7px">
    <div style="font-size:9px;font-weight:500">Loved by Families Everywhere</div>
    <div style="font-size:2.6px;margin:2px 0 4px;color:#e6f0ff">Join over 10 million people preserving their family history.</div>
    <span class="btn light">Start Free Today</span> <span class="btn ghost" style="border-color:#cfe">View Pricing</span>
  </div>

  <footer class="footer" style="top:899px;height:80px">
    <div class="logo">memora.ai</div><p class="about">AI-powered photo restoration and animation platform. Preserve your family's most precious memories.</p>
    <div class="socials"><span></span><span></span><span></span></div>
    <div class="col" style="left:114px"><b>PRODUCT</b><br>Restore Photos<br>Colorize<br>Animate<br>Story Videos</div>
    <div class="col" style="left:171px"><b>COMPANY</b><br>About<br>Blog<br>Careers<br>Contact</div>
    <div class="col" style="left:221px"><b>LEGAL</b><br>Privacy Policy<br>Terms of Service<br>Cookie Policy</div>
    <div class="legal"><span>© 2026 memora.ai. All rights reserved.</span><span>Made with care for every memory.</span></div>
  </footer>
</section>

<!-- IMAGES -->
<section class="page" style="left:318px;top:110px;width:269px;height:457px">
  <nav class="nav"><span class="logo">memora.ai</span><span class="links"><span>Home</span><span class="on">Images</span><span>Video animations</span><span>Studio</span></span><span class="auth">Sign in <span class="btn">Get Started</span></span></nav>
  <h2 class="h2 center" style="top:22px">Three steps to stunning results</h2>
  <p class="sub center" style="top:32px;padding:0 80px">From upload to download in under 30 seconds. No technical knowledge required.</p>
  <div class="card step" style="left:22px;top:48px;width:70px;height:40px"><i class="icon"></i><b>Upload Your Photo</b><p>Drag and drop or select any old, faded, or black &amp; white photo. JPG, PNG, HEIC up to 20MB.</p></div>
  <div class="card step" style="left:99px;top:48px;width:70px;height:40px"><i class="icon"></i><b>AI Restoration</b><p>Our deep learning models restore your photo, repair damage, sharpen details, and add color.</p></div>
  <div class="card step" style="left:176px;top:48px;width:70px;height:40px"><i class="icon"></i><b>Download &amp; Share</b><p>Get your restored photo in high resolution within seconds. Download and share or order a print.</p></div>
  <div style="left:0;top:95px;width:269px;height:127px;background:var(--band)"></div>
  <p class="eyebrow center" style="top:106px">Try it free</p>
  <h2 class="h2 center" style="top:112px">Restore Your Photo Now</h2>
  <p class="sub center" style="top:121px">Upload any old photo and watch AI bring it back to life in seconds.</p>
  <div class="drop" style="left:22px;top:135px;width:101px;height:71px"><i class="icon"></i><b>Drop your photo here</b><small>or click to browse your files</small><span class="btn">Choose Photo</span><small>Supports JPG, PNG, HEIC · up to 20MB</small></div>
  <div class="photo grey" role="img" aria-label="Empty before and after comparison preview" style="left:146px;top:135px;width:101px;height:71px"></div>
  <div style="left:196px;top:135px;width:.6px;height:71px;background:var(--blue)"></div>
  <p class="eyebrow center" style="top:231px;color:var(--teal)">Gallery</p>
  <h2 class="h2 center" style="top:237px">Incredible transformations</h2>
  <p class="sub center" style="top:246px">Hover over each photo to reveal the colorized restoration.</p>
  <div class="photo" role="img" aria-label="Two elderly men on a bench" style="left:22px;top:264px;width:73px;height:47px"></div>
  <div class="photo blue" role="img" aria-label="Group of men playing cards outdoors" style="left:98px;top:264px;width:73px;height:47px"></div>
  <div class="photo" role="img" aria-label="Elderly men talking on a street" style="left:174px;top:264px;width:73px;height:47px;background:linear-gradient(135deg,#e2ddd3,#6a5846)"></div>
  <div class="photo" role="img" aria-label="Man leaning on a vintage sports car" style="left:22px;top:315px;width:73px;height:47px;background:linear-gradient(135deg,#9a9b7a,#1e1e1e)"></div>
  <div class="photo" role="img" aria-label="Antique red car by a stone building" style="left:98px;top:315px;width:73px;height:47px;background:linear-gradient(135deg,#8a7b66,#5a2a22)"></div>
  <div class="photo" role="img" aria-label="Elderly couple seated together" style="left:174px;top:315px;width:73px;height:47px;background:linear-gradient(135deg,#b59a78,#3e3228)"></div>
  <footer class="footer" style="top:377px;height:80px">
    <div class="logo">memora.ai</div><p class="about">AI-powered photo restoration and animation platform. Preserve your family's most precious memories.</p>
    <div class="socials"><span></span><span></span><span></span></div>
    <div class="col" style="left:115px"><b>PRODUCT</b><br>Restore Photos<br>Colorize<br>Animate<br>Story Videos</div>
    <div class="col" style="left:171px"><b>COMPANY</b><br>About<br>Blog<br>Careers<br>Contact</div>
    <div class="col" style="left:221px"><b>LEGAL</b><br>Privacy Policy<br>Terms of Service<br>Cookie Policy</div>
    <div class="legal"><span>© 2026 memora.ai. All rights reserved.</span><span>Made with care for every memory.</span></div>
  </footer>
</section>

<!-- VIDEO ANIMATIONS -->
<section class="page" style="left:613px;top:110px;width:269px;height:457px">
  <nav class="nav"><span class="logo">memora.ai</span><span class="links"><span>Home</span><span>Images</span><span class="on">Video animations</span><span>Studio</span></span><span class="auth">Sign in <span class="btn">Get Started</span></span></nav>
  <h2 class="h2 center" style="top:22px">Three steps to motion</h2>
  <p class="sub center" style="top:32px;padding:0 80px">From still to stunning in under a minute. No creative skills required.</p>
  <div class="card step" style="left:22px;top:48px;width:70px;height:40px"><i class="icon"></i><b>Upload Your Photo</b><p>Drag and drop any JPEG, PNG, or WEBP image. Works best with portraits and landscapes.</p></div>
  <div class="card step" style="left:99px;top:48px;width:70px;height:40px"><i class="icon"></i><b>Choose a style</b><p>Pick from 50+ animation presets: cinematic parallax, flowing water, swaying trees, and more.</p></div>
  <div class="card step" style="left:176px;top:48px;width:70px;height:40px"><i class="icon"></i><b>Export &amp; share</b><p>Download your animated clip as MP4 or GIF in full resolution, ready to share anywhere.</p></div>
  <div style="left:0;top:95px;width:269px;height:127px;background:var(--band)"></div>
  <p class="eyebrow center" style="top:106px">Try it free</p>
  <h2 class="h2 center" style="top:112px">Animated video clip in seconds</h2>
  <p class="sub center" style="top:121px;padding:0 80px">Turn any still image into a breathtaking animated video clip in seconds.</p>
  <div class="drop" style="left:22px;top:140px;width:112px;height:71px"><i class="icon"></i><b>Drop your photo here</b><small>or click to browse your files</small><span class="btn">Choose Photo</span><small>Supports JPG, PNG, HEIC · up to 20MB</small></div>
  <div class="label" style="left:142px;top:140px">Duration:</div>
  <span class="chip on" style="left:142px;top:147px">5 seconds</span>
  <div class="field" style="left:142px;top:157px;width:105px;height:41px">Describe motion or upload audio...</div>
  <div class="grad-btn" style="left:142px;top:204px;width:105px;height:7px">Upload &amp; Animate</div>
  <p class="eyebrow center" style="top:231px;color:var(--teal)">Gallery</p>
  <h2 class="h2 center" style="top:237px">See it in action</h2>
  <p class="sub center" style="top:246px;padding:0 95px">Real photos animated. Hover to preview the motion.</p>
  <div class="photo" role="img" aria-label="Two elderly men on a bench" style="left:22px;top:264px;width:73px;height:47px"></div>
  <div class="photo blue" role="img" aria-label="Group of men playing cards outdoors" style="left:98px;top:264px;width:73px;height:47px"></div>
  <div class="photo" role="img" aria-label="Elderly men talking on a street" style="left:174px;top:264px;width:73px;height:47px;background:linear-gradient(135deg,#e2ddd3,#6a5846)"></div>
  <div class="photo" role="img" aria-label="Man leaning on a vintage sports car" style="left:22px;top:315px;width:73px;height:47px;background:linear-gradient(135deg,#9a9b7a,#1e1e1e)"></div>
  <div class="photo" role="img" aria-label="Antique red car by a stone building" style="left:98px;top:315px;width:73px;height:47px;background:linear-gradient(135deg,#8a7b66,#5a2a22)"></div>
  <div class="photo" role="img" aria-label="Elderly couple seated together" style="left:174px;top:315px;width:73px;height:47px;background:linear-gradient(135deg,#b59a78,#3e3228)"></div>
  <footer class="footer" style="top:377px;height:80px">
    <div class="logo">memora.ai</div><p class="about">AI-powered photo restoration and animation platform. Preserve your family's most precious memories.</p>
    <div class="socials"><span></span><span></span><span></span></div>
    <div class="col" style="left:115px"><b>PRODUCT</b><br>Restore Photos<br>Colorize<br>Animate<br>Story Videos</div>
    <div class="col" style="left:171px"><b>COMPANY</b><br>About<br>Blog<br>Careers<br>Contact</div>
    <div class="col" style="left:221px"><b>LEGAL</b><br>Privacy Policy<br>Terms of Service<br>Cookie Policy</div>
    <div class="legal"><span>© 2026 memora.ai. All rights reserved.</span><span>Made with care for every memory.</span></div>
  </footer>
</section>

<!-- STUDIO -->
<section class="page" style="left:908px;top:110px;width:269px;height:503px">
  <nav class="nav"><span class="logo">memora.ai</span><span class="links"><span>Home</span><span>Images</span><span>Video animations</span><span class="on">Studio</span></span><span class="auth">Sign in <span class="btn">Get Started</span></span></nav>
  <h2 class="h2 center" style="top:22px">Turn Moments into Meaningful Stories</h2>
  <p class="sub center" style="top:32px;padding:0 85px">Bring your restored photos and animations together into one cinematic experience.</p>

  <div class="card" style="left:22px;top:50px;width:225px;height:60px;background:var(--band)"></div>
  <div class="label" style="left:28px;top:55px;font-size:2.6px">Drag images and videos to storyboard</div>
  <span class="chip on" style="left:202px;top:54px;background:#fff;color:var(--blue);border-color:#fff">Images</span>
  <span class="chip" style="left:225px;top:54px">Videos</span>
  <div class="photo blue" role="img" aria-label="Family portrait thumbnail" style="left:28px;top:64px;width:39px;height:27px"></div>
  <div class="photo" role="img" aria-label="Portrait of man with child thumbnail" style="left:72px;top:64px;width:39px;height:27px"></div>
  <div class="photo warm" role="img" aria-label="Riders before old buildings thumbnail" style="left:116px;top:64px;width:39px;height:27px"></div>
  <div class="photo" role="img" aria-label="Man beside vintage car thumbnail" style="left:159px;top:64px;width:39px;height:27px;background:linear-gradient(140deg,#d8d6d0,#3a4a6e 60%,#222)"></div>
  <div class="photo" role="img" aria-label="Elderly men on a bench thumbnail" style="left:203px;top:64px;width:39px;height:27px"></div>
  <span class="btn" style="left:28px;top:96px;height:5px">+ Add</span>
  <svg style="left:222px;top:97px" width="20" height="4" viewBox="0 0 20 4"><path d="M5 2H0M1.5 .5 0 2l1.5 1.5M15 2h5M18.5 .5 20 2l-1.5 1.5" stroke="#8290b3" stroke-width=".5" fill="none"/></svg>

  <div class="card" style="left:22px;top:117px;width:225px;height:137px;background:var(--band)"></div>
  <div class="label" style="left:28px;top:123px;font-size:2.6px">Drag images and videos to storyboard</div>
  <div class="label" style="left:137px;top:123px;font-size:2.6px">PREVIEW</div>
  <span class="chip" style="left:222px;top:122px">Clear All</span>
  <div style="left:28px;top:133px;width:103px;height:60px;display:grid;grid-template-columns:repeat(4,1fr);grid-template-rows:repeat(3,1fr);gap:2px">
    <div class="photo" role="img" aria-label="Storyboard clip"></div><div class="photo blue" role="img" aria-label="Storyboard clip"></div><div class="photo" role="img" aria-label="Storyboard clip"></div><div class="photo warm" role="img" aria-label="Storyboard clip"></div>
    <div class="photo blue" role="img" aria-label="Storyboard clip"></div><div class="photo" role="img" aria-label="Storyboard clip" style="background:linear-gradient(140deg,#d8d6d0,#3a4a6e)"></div><div class="photo" role="img" aria-label="Storyboard clip"></div><div class="photo" role="img" aria-label="Storyboard clip"></div>
    <div class="photo" role="img" aria-label="Storyboard clip" style="background:linear-gradient(135deg,#9a9b7a,#1e1e1e)"></div><div style="border:.4px dashed #2d3f6a;border-radius:2px"></div><div style="border:.4px dashed #2d3f6a;border-radius:2px"></div><div style="border:.4px dashed #2d3f6a;border-radius:2px"></div>
  </div>
  <svg style="left:77px;top:196px" width="5" height="5" viewBox="0 0 5 5"><circle cx="2.5" cy="2.5" r="2.2" fill="none" stroke="#8290b3" stroke-width=".4"/><path d="M2.5 1.2v2.6M1.2 2.5h2.6" stroke="#8290b3" stroke-width=".4"/></svg>
  <div style="left:28px;top:205px;width:103px;height:.5px;background:#2d3f6a"></div>
  <div class="photo" role="img" aria-label="Preview: two elderly men seated on a bench" style="left:137px;top:133px;width:105px;height:73px"></div>
  <div class="label" style="left:28px;top:210px;font-size:2.6px">Add Music</div>
  <span class="chip on" style="left:28px;top:216px">Neutral</span>
  <span class="chip" style="left:42px;top:216px">Emotional</span>
  <span class="chip" style="left:62px;top:216px">Happy</span>
  <div class="field" style="left:28px;top:225px;width:103px;height:6px;padding:1.2px 3px;font-size:2px;color:var(--muted);display:flex;justify-content:space-between"><span>◂ ● ▸ &nbsp; Paper Lantern Return</span><span>4:32</span></div>
  <div style="left:28px;top:243px;font-size:2px;color:var(--muted);display:flex;align-items:center;gap:2px"><span style="width:3px;height:3px;border:.4px solid #8290b3;border-radius:.5px;display:inline-block"></span>No sound</div>
  <div class="field" style="left:137px;top:215px;width:105px;height:19px">Write your story caption...</div>
  <div class="grad-btn" style="left:137px;top:240px;width:105px;height:7px">Generate Story — 10 credits</div>

  <div class="card" style="left:22px;top:262px;width:225px;height:71px;background:var(--band)"></div>
  <div class="photo warm" role="img" aria-label="Story video thumbnail: riders before old buildings" style="left:33px;top:268px;width:115px;height:60px"></div>
  <div class="action" style="left:161px;top:275px">Edit</div>
  <div class="action" style="left:161px;top:287px">Download</div>
  <div class="action danger" style="left:161px;top:299px">Delete</div>
  <div style="left:161px;top:309px;font-size:2.7px;color:#c8d0e6;line-height:1.3">Duration: 50s<br>Music: Emotional</div>

  <div class="card" style="left:22px;top:341px;width:225px;height:71px;background:var(--band)"></div>
  <div class="photo blue" role="img" aria-label="Story video thumbnail: family portrait" style="left:33px;top:347px;width:115px;height:60px"></div>
  <div class="action" style="left:161px;top:354px">Edit</div>
  <div class="action" style="left:161px;top:366px">Download</div>
  <div class="action danger" style="left:161px;top:378px">Delete</div>
  <div style="left:161px;top:388px;font-size:2.7px;color:#c8d0e6;line-height:1.3">Duration: 1m 0s<br>Music: Neutral</div>

  <footer class="footer" style="top:422px;height:81px">
    <div class="logo">memora.ai</div><p class="about">AI-powered photo restoration and animation platform. Preserve your family's most precious memories.</p>
    <div class="socials"><span></span><span></span><span></span></div>
    <div class="col" style="left:114px"><b>PRODUCT</b><br>Restore Photos<br>Colorize<br>Animate<br>Story Videos</div>
    <div class="col" style="left:171px"><b>COMPANY</b><br>About<br>Blog<br>Careers<br>Contact</div>
    <div class="col" style="left:221px"><b>LEGAL</b><br>Privacy Policy<br>Terms of Service<br>Cookie Policy</div>
    <div class="legal"><span>© 2026 memora.ai. All rights reserved.</span><span>Made with care for every memory.</span></div>
  </footer>
</section>

</body>
</html>
```